Business Card Design

We are a state licensed general contractor on the south east coast of Florida. We are a remodeling and home repairs business that have been in business for 14 years. Since we are located on the coast and our business name is Ridgeline Builders of Pine Hollow, Inc, we would like a "Ridgeline" themed design that would appeal to more affluent customers. I would like to see light blue colors with waves incorporated into the design. I would also like the design to communicate a modern, confident, responsible company character.

Industry/Entity Type

Contractor

Contact Information for Business Card

Tim Wexler 555-274-9183

```html
<!DOCTYPE html>
<html lang="en">
<head>
<meta charset="utf-8">
<title>Ridgeline Builders – Business Card</title>
<link href="https://fonts.googleapis.com/css2?family=Open+Sans:wght@300;400;600;700&display=swap" rel="stylesheet">
<style>
  :root {
    --navy: #164a80;
    --navy-deep: #12406f;
    --sky: #2f9ad8;
    --rule: #8a8f96;
    --paper: #ffffff;
    --muted: #6d737a;
    --backdrop: #e4e6e9;
  }
  * { margin: 0; padding: 0; box-sizing: border-box; }
  html, body {
    width: 1200px; height: 848px; overflow: hidden;
    background: var(--backdrop);
    font-family: "Open Sans", Arial, sans-serif;
  }
  .card {
    position: absolute; left: 100px; top: 138px;
    width: 1000px; height: 572px;
    border-radius: 26px; overflow: hidden;
    background: var(--paper);
    box-shadow: 0 10px 30px rgba(0,0,0,.18);
  }
  .card-top { position: absolute; inset: 0 0 auto 0; height: 340px; }
  .card-rule { position: absolute; left: 0; right: 0; top: 340px; height: 5px; background: var(--rule); }
  .card-band { position: absolute; left: 0; right: 0; top: 345px; bottom: 0; background: var(--navy); }

  .brand {
    position: absolute; left: 70px; top: 92px;
    display: flex; align-items: center; gap: 22px;
  }
  .brand-dot { width: 34px; height: 34px; border-radius: 50%; background: var(--sky); }
  .brand-name {
    font-weight: 700; font-size: 70px; line-height: 1;
    color: var(--navy-deep); letter-spacing: -1px;
  }
  .license {
    position: absolute; right: 70px; top: 255px;
    font-size: 26px; color: var(--navy); letter-spacing: 1px;
  }
  .person {
    position: absolute; left: 70px; top: 270px;
    display: flex; align-items: center; gap: 16px;
  }
  .person-name { font-weight: 700; font-size: 38px; color: var(--navy); letter-spacing: 1px; }
  .person-divider { width: 2px; height: 36px; background: var(--muted); }
  .person-role { font-weight: 300; font-size: 22px; color: var(--muted); letter-spacing: 1px; }

  .contact, .address {
    position: absolute; color: var(--paper); font-size: 27px; line-height: 40px;
  }
  .contact { left: 70px; top: 382px; }
  .contact b { font-weight: 600; }
  .address { right: 70px; top: 382px; text-align: left; }
</style>
</head>
<body>
  <div class="card">
    <div class="card-top">
      <div class="brand">
        <span class="brand-dot"></span>
        <span class="brand-name">Ridgeline Builders</span>
      </div>
      <div class="license">CGC048213</div>
      <div class="person">
        <span class="person-name">TIM WEXLER</span>
        <span class="person-divider"></span>
        <span class="person-role">OWNER</span>
      </div>
    </div>
    <div class="card-rule"></div>
    <div class="card-band">
    </div>
    <div class="contact">
      <div><b>Cell</b> 555-274-9183</div>
      <div><b>Office</b> 555-318.6040</div>
      <div><b>Fax</b> 555-318.7152</div>
      <div>ridgeline.tw@mail.com</div>
    </div>
    <div class="address">
      <div>4280 Alder Bend Way</div>
      <div>Pine Hollow, FL 30000</div>
    </div>
  </div>
</body>
</html>
```